Modern Business Cards and Stationary for a Dentist
Derek M. Thalby, DDS, PLLC
Modern Business Cards and Stationary for a Dentist - Health
Creative Brief
Professional
Derek M. Thalby, DDS and Joanne R. Thalby, DDS
General Dentistry
318 West Brannig Street Fredericksburg, TX 78539
thalbydds@mailvesta.com
I need business cards and letterhead. There are two doctors in the office, please put both names on the business cards. They do not need separate cards. Please put the phone number for After Hours underneath the fax number. That number is 830-555-4172. I would like the front of the card to be colorful. But I would like the back of the card to be predominately white with color accents so that it is easy to read once the appointment information is written on it. Please try to incorporate the logo on the back as well.
Appointment card on the back. Line for the name. Under the line "Has an appointment on" then checkboxes for days of the week M,T,W,Th,F. Then another line for the Date and Time of the appointment and another line for Notes. Underneath everything the sentence: If you are unable to keep this appointment, please notify us within 24 hours.

```html
<!DOCTYPE html>
<html lang="en">
<head>
<meta charset="utf-8">
<title>Derek M. Thalby, DDS, PLLC — Stationery</title>
<link rel="stylesheet" href="https://fonts.googleapis.com/css2?family=Cinzel:wght@500&family=Cormorant+Garamond:ital,wght@1,500&family=Open+Sans:wght@400;600&display=swap">
<style>
  :root{
    --bg:#e7e7e9;
    --paper:#ffffff;
    --maroon:#86213f;
    --ink:#4a4a4d;
    --soft:#8c8c90;
    --rule:#c9c9cc;
    --shadow:0 2px 6px rgba(0,0,0,.12);
  }
  *{box-sizing:border-box;margin:0;padding:0}
  html,body{width:1200px;height:936px;overflow:hidden;background:var(--bg)}
  body{position:relative;font-family:"Open Sans",Arial,sans-serif;color:var(--ink)}
  .sheet{position:absolute;background:var(--paper);box-shadow:var(--shadow);overflow:hidden}
  .brand-name{font-family:"Cinzel",Georgia,serif;font-weight:500;color:var(--ink);white-space:nowrap}
  .brand-dot{display:inline-block;border-radius:50%;background:var(--maroon);vertical-align:middle;flex:none}
  .tagline{font-family:"Cormorant Garamond",Georgia,serif;font-style:italic;font-weight:500;color:var(--maroon);white-space:nowrap}

  /* Letterhead */
  .letterhead{left:180px;top:66px;width:392px;height:536px}
  .letterhead .masthead{position:absolute;left:28px;top:24px;display:flex;align-items:center;gap:7px}
  .letterhead .brand-dot{width:18px;height:18px}
  .letterhead .brand-name{font-size:10px}
  .letterhead .tagline{font-size:7px;display:block;margin-top:1px}
  .letter-body{position:absolute;left:28px;top:78px;width:318px;font-size:5.4px;line-height:1.55;color:var(--soft)}
  .letter-body p{margin-bottom:9px}
  .letter-body .signature{width:40px;height:16px;background:linear-gradient(90deg,#d8d8da,#bfbfc3);margin:4px 0 5px}
  .letter-band{position:absolute;left:0;right:0;bottom:10px;height:14px;background:var(--maroon);color:#fff;font-size:5px;display:flex;align-items:center;gap:14px;padding-left:28px;white-space:nowrap}

  /* Presentation sheet */
  .cover{left:637px;top:43px;width:418px;height:561px}
  .cover .identity{position:absolute;left:0;right:0;top:222px;text-align:center}
  .cover .brand-dot{width:70px;height:70px;display:block;margin:0 auto 16px}
  .cover .brand-name{font-size:17px;letter-spacing:.5px}
  .cover .tagline{font-size:12px;margin-top:4px}
  .cover-band{position:absolute;left:0;right:0;top:518px;height:30px;background:var(--maroon);color:#fff;font-family:"Cinzel",Georgia,serif;font-size:12px;letter-spacing:2px;display:flex;align-items:center;justify-content:flex-end;padding-right:36px;white-space:nowrap}

  /* Business card */
  .card{width:208px}
  .card .brand-dot{width:9px;height:9px}
  .card .brand-name{font-size:6px}
  .card-front{left:41px;top:672px;height:78px}
  .card-front .masthead{position:absolute;left:10px;top:8px;display:flex;align-items:center;gap:4px}
  .card-front .doctors{position:absolute;left:10px;top:21px;font-size:4px;color:var(--soft);white-space:nowrap}
  .card-band{position:absolute;left:0;right:0;top:32px;height:20px;background:var(--maroon);color:#fff;font-size:3.8px;line-height:1.45;padding:3px 10px}
  .card-front .hours{position:absolute;left:10px;top:57px;font-size:3.8px;color:var(--soft);line-height:1.45}

  .card-back{left:41px;top:774px;height:126px;padding:10px 12px}
  .card-back .masthead{display:flex;align-items:center;gap:4px;margin-bottom:8px}
  .field{display:flex;align-items:flex-end;gap:3px;font-size:4px;color:var(--ink);margin-bottom:8px}
  .field .line{flex:1;border-bottom:.6px solid var(--rule);height:5px}
  .days{display:flex;gap:9px;font-size:4px;margin:-3px 0 8px}
  .days span{display:flex;align-items:center;gap:2px}
  .days i{display:inline-block;width:4px;height:4px;border:.6px solid var(--maroon)}
  .card-back .notice{font-size:3.4px;color:var(--maroon);text-align:center;margin-top:4px}

  /* Envelopes */
  .envelope-dl{left:266px;top:672px;width:401px;height:221px}
  .envelope-dl .masthead{position:absolute;left:16px;top:16px;display:flex;align-items:center;gap:5px}
  .envelope-dl .brand-dot{width:13px;height:13px}
  .envelope-dl .brand-name{font-size:7.5px}
  .envelope-dl .return{position:absolute;left:16px;top:37px;font-size:4.2px;color:var(--soft);line-height:1.5}

  .envelope-flap{left:738px;top:672px;width:422px;height:221px}
  .envelope-flap svg{position:absolute;inset:0}
  .envelope-flap .seal{position:absolute;left:0;right:0;top:64px;text-align:center}
  .envelope-flap .brand-dot{width:13px;height:13px;display:block;margin:0 auto 4px}
  .envelope-flap .brand-name{font-size:5px}
</style>
</head>
<body>

<section class="sheet letterhead" aria-label="Letterhead">
  <header class="masthead">
    <span class="brand-dot"></span>
    <div>
      <span class="brand-name">Derek M. Thalby, DDS, PLLC</span>
      <span class="tagline">Gentle Care for Every Smile in the Family.</span>
    </div>
  </header>
  <div class="letter-body">
    <p>March 4, 2024<br>Dear Patient,<br>Hill Building, 3rd Street, Town Name</p>
    <p>Thank you for choosing our practice for your family dental care. We are pleased to confirm your next visit and look forward to seeing you soon. Please bring your insurance card and a current list of medications so we can keep your records up to date.</p>
    <p>Our team offers cleanings, fillings, crowns and whitening in a calm and friendly setting.</p>
    <p>If you have questions about your treatment plan or billing, our front desk staff will gladly help during regular office hours.</p>
    <p>We value your trust and thank you for letting us care for your smile.</p>
    <p>Best Regards,</p>
    <div class="signature" role="img" aria-label="Handwritten signature"></div>
    <p>Derek M. Thalby<br>Dentist<br>Hill Building, 3rd Street, Town Name</p>
  </div>
  <footer class="letter-band">
    <span>318 West Brannig Street, Fredericksburg, TX 78539</span>
    <span>830-555-4172</span>
    <span>thalbydds@mailvesta.com</span>
  </footer>
</section>

<section class="sheet cover" aria-label="Presentation sheet">
  <div class="identity">
    <span class="brand-dot"></span>
    <div class="brand-name">Derek M. Thalby, DDS, PLLC</div>
    <div class="tagline">Gentle Care for Every Smile in the Family.</div>
  </div>
  <div class="cover-band">www.ThalbyDentalCare.com</div>
</section>

<section class="sheet card card-front" aria-label="Business card front">
  <div class="masthead"><span class="brand-dot"></span><span class="brand-name">Derek M. Thalby, DDS, PLLC</span></div>
  <div class="doctors">Derek M. Thalby, DDS &nbsp;·&nbsp; Joanne R. Thalby, DDS</div>
  <div class="card-band">
    318 West Brannig Street, Fredericksburg, TX 78539<br>
    thalbydds@mailvesta.com
  </div>
  <div class="hours">Phone: 830-555-4172<br>After Hours: 830-555-4172</div>
</section>

<section class="sheet card card-back" aria-label="Appointment card">
  <div class="masthead"><span class="brand-dot"></span><span class="brand-name">Derek M. Thalby, DDS, PLLC</span></div>
  <div class="field">Name<span class="line"></span></div>
  <div class="field">Has an appointment on</div>
  <div class="days"><span><i></i>M</span><span><i></i>T</span><span><i></i>W</span><span><i></i>Th</span><span><i></i>F</span></div>
  <div class="field">Date &amp; Time<span class="line"></span></div>
  <div class="field">Notes<span class="line"></span></div>
  <p class="notice">If you are unable to keep this appointment, please notify us within 24 hours.</p>
</section>

<section class="sheet envelope-dl" aria-label="Envelope front">
  <div class="masthead"><span class="brand-dot"></span><span class="brand-name">Derek M. Thalby, DDS, PLLC</span></div>
  <div class="return">318 West Brannig Street<br>Fredericksburg, TX 78539</div>
</section>

<section class="sheet envelope-flap" aria-label="Envelope back">
  <svg width="422" height="221" viewBox="0 0 422 221" aria-hidden="true">
    <polyline points="0,0 211,92 422,0" fill="none" stroke="#c9c9cc" stroke-width="1"/>
  </svg>
  <div class="seal"><span class="brand-dot"></span><span class="brand-name">Derek M. Thalby, DDS, PLLC</span></div>
</section>

</body>
</html>
```